Cards for Employees

We are looking for an Anniversary and a Birthday card to send to our employees. 2 designs.
We send these cards to our employees based on number of years they work at the company.
Check out our website for more info.
www.BrookfieldServices.example
Target Market(s)
Our Employees -
Font styles to use
Sans Serif
Colors
Designer to choose colors to be used in the design.
Requirements
Must have
- Anniversary card - appreciation for hard work and dedication
Logo - no changes

```html
<!DOCTYPE html>
<html lang="en">
<head>
<meta charset="utf-8">
<title>Happy Anniversary – Brookfield Services</title>
<link rel="stylesheet" href="https://fonts.googleapis.com/css2?family=Caladea&family=Tinos&family=Pinyon+Script&display=swap">
<style>
  :root {
    --page-bg: #ffffff;
    --night: #070304;
    --ember: #3a1408;
    --glow: #c8782c;
    --bulb-core: #f2c070;
    --ink-light: #ffffff;
  }
  html, body {
    margin: 0;
    padding: 0;
    width: 1200px;
    height: 871px;
    overflow: hidden;
    background: var(--page-bg);
  }
  .canvas {
    position: relative;
    width: 1200px;
    height: 871px;
  }
  .card {
    position: absolute;
    left: 162px;
    top: 115px;
    width: 885px;
    height: 650px;
    overflow: hidden;
    background: var(--night);
  }
  .card-photo {
    position: absolute;
    inset: 0;
    background:
      radial-gradient(ellipse 150px 230px at 710px 260px, var(--bulb-core) 0%, var(--glow) 30%, rgba(90,30,10,0.5) 65%, rgba(0,0,0,0) 100%),
      radial-gradient(ellipse 260px 160px at 260px 170px, rgba(150,30,20,0.55) 0%, rgba(0,0,0,0) 100%),
      radial-gradient(ellipse 300px 120px at 760px 580px, rgba(120,80,40,0.35) 0%, rgba(0,0,0,0) 100%),
      linear-gradient(160deg, var(--ember) 0%, var(--night) 55%, var(--night) 100%);
  }
  .brand-name {
    position: absolute;
    left: 0;
    width: 720px;
    top: 326px;
    text-align: center;
    font-family: "Caladea", serif;
    font-size: 22px;
    letter-spacing: 1px;
    text-transform: uppercase;
    color: var(--ink-light);
  }
  .headline-happy {
    position: absolute;
    left: 0;
    width: 720px;
    top: 385px;
    margin: 0;
    text-align: center;
    font-family: "Tinos", serif;
    font-weight: 400;
    font-size: 98px;
    line-height: 1;
    color: var(--ink-light);
  }
  .headline-anniversary {
    position: absolute;
    left: 40px;
    top: 440px;
    margin: 0;
    font-family: "Pinyon Script", cursive;
    font-weight: 400;
    font-size: 112px;
    line-height: 1.1;
    color: var(--ink-light);
    white-space: nowrap;
  }
  .tagline {
    position: absolute;
    left: 56px;
    top: 546px;
    margin: 0;
    font-family: "Caladea", serif;
    font-size: 28px;
    color: var(--ink-light);
    white-space: nowrap;
  }
</style>
</head>
<body>
  <div class="canvas">
    <section class="card">
      <div class="card-photo" role="img" aria-label="Photograph of a glowing vintage filament light bulb hanging against a dark background with blurred colourful bokeh lights"></div>
      <div class="brand-name">Brookfield Services</div>
      <h1 class="headline-happy">HAPPY</h1>
      <h2 class="headline-anniversary">Anniversary</h2>
      <p class="tagline">Appreciation for hard work and dedication!</p>
    </section>
  </div>
</body>
</html>
```